CV brochure for Top Management Position

I need me to introduce myself a brochure design for a CV brochure in. So sort of a resume in booklet format. The design should be serious for a convey on the other, the viewer that I stand for the new world of digitization. The brochure is intended to convey that I am a "Digital Leader". With the brochure boards, boards of directors and decision makers of enterprises should pay attention to my person. It must not be a 0815 design of the rod. The design should already be addressed with the front page of the topic Digital Leader, since the front page usually is the decisive criterion whether to continue dealing with the person or not. I am now CIO (IT manager) and wants to move with the brochure myself from this technique corner out and thus make it interesting for other positions. The positions are in absolute top management, the board, management, supervisory anchored and deal primarily with the digital transformation and the new digital world. So should appear with security on the front page a concise picture of me. but I am also very open to any alternative proposal brochure. Here you can see my current CV with picture and the basic content. The brochure is even more responsive to the social skills and not only to the technical projects implemented as before.

Target Market(s)

Top management, CxO level, supervisory boards, large companies, large Mittlestandsunternehmen

Industry/Entity Type

Management

Font styles to use
Serif
Sans Serif

Requirements
Must have
• see description
Nice to have
• see description
Should not have
• see description

```html
<!DOCTYPE html>
<html lang="de">
<head>
<meta charset="utf-8">
<title>Lebenslauf Broschüre – Digital Leader</title>
<link href="https://fonts.googleapis.com/css2?family=Fira+Sans+Condensed:ital,wght@0,300;0,400;0,600;0,700;1,700&display=swap" rel="stylesheet">
<style>
:root{
  --backdrop:#2a2c30;
  --paper:#ffffff;
  --teal:#2fb6c7;
  --teal-dark:#1d97a9;
  --teal-light:#6fd0dc;
  --yellow:#f6b90e;
  --ink:#2b2b2b;
  --ink-soft:#555;
  --rule:#9a9a9a;
}
*{box-sizing:border-box;margin:0;padding:0}
html,body{width:830px;height:1200px;overflow:hidden}
body{background:var(--backdrop);font-family:"Fira Sans Condensed",Arial,sans-serif;color:var(--ink);position:relative}
.page{position:absolute;width:375px;height:485px;background:var(--paper);overflow:hidden}
.page--cover{left:30px;top:103px}
.page--2{left:430px;top:103px}
.page--3{left:30px;top:638px}
.page--4{left:430px;top:638px}
.deco{position:absolute;left:0;top:0}

/* cover */
.sidebar{position:absolute;left:10px;top:26px;width:130px;height:424px;background:var(--teal);color:#fff}
.portrait{position:absolute;left:23px;top:22px;width:84px;height:84px;border-radius:50%;border:3px solid #fff;background:radial-gradient(circle at 50% 40%,#d9d9d9,#8c8c8c 70%,#5a5a5a)}
.role-title{position:absolute;left:0;width:130px;top:130px;text-align:center;font-size:13.5px;font-weight:300;line-height:15px;padding-bottom:6px}
.role-title::after{content:"";position:absolute;left:10px;right:10px;bottom:0;border-bottom:1px solid rgba(255,255,255,.8)}
.facts{position:absolute;left:10px;top:174px;width:115px;font-size:5.6px;line-height:7px}
.facts dt{font-weight:700;margin-top:5px}
.facts dd{font-weight:300}
.overview{position:absolute;left:148px;top:153px;width:208px}
.section-title{font-weight:700;font-style:italic;font-size:9.5px;color:var(--ink);padding-bottom:3px;border-bottom:1px solid var(--rule);margin-bottom:8px}
.overview ul{list-style:none}
.overview li{font-size:6.3px;line-height:11px;color:var(--ink-soft);margin-bottom:10px;padding-left:5px;position:relative}
.overview li::before{content:"";position:absolute;left:0;top:4.5px;width:3px;height:3px;border-radius:50%;background:var(--ink)}
.overview b{color:var(--ink);font-weight:600}

/* inner pages */
.running-head{position:absolute;left:21px;top:11px;color:#fff;font-size:5.6px;line-height:6.5px;font-weight:300}
.running-head strong{display:block;font-size:9.5px;line-height:11px;font-weight:700;font-style:italic}
.page-no{position:absolute;right:16px;bottom:10px;width:15px;height:15px;border:1.2px solid #fff;color:#fff;font-size:8px;font-weight:700;text-align:center;line-height:13px}
.content{position:absolute;left:22px;width:335px}
.heading-box{display:inline-block;border:1.2px solid var(--ink);padding:1px 5px;font-weight:700;font-style:italic;font-size:9.5px;margin:0 0 8px 0}
.heading-box--wide{width:104px;text-align:center}
.entry{display:grid;grid-template-columns:51px 1fr;font-size:5.6px;line-height:7.8px;color:var(--ink-soft)}
.entry .when{font-weight:700;color:var(--ink);padding-top:1px}
.entry .what{border-left:1px solid var(--rule);padding:1px 0 16px 7px}
.entry .what b{color:var(--ink);font-weight:600}
.entry .label{color:var(--ink);font-weight:600;margin-top:6px}
.entry ul{list-style:none}
.entry li{padding-left:4px;position:relative}
.entry li::before{content:"";position:absolute;left:0;top:3.2px;width:2.2px;height:2.2px;border-radius:50%;background:var(--ink)}
.kv{display:grid;grid-template-columns:68px 1fr}
.sign-off{font-weight:700;font-style:italic;color:var(--ink);font-size:5.8px}
</style>
</head>
<body>

<!-- Cover -->
<section class="page page--cover">
  <aside class="sidebar">
    <svg class="deco" width="130" height="424" viewBox="0 0 130 424" aria-hidden="true">
      <polygon points="72,22 130,0 130,14 96,24" fill="var(--yellow)"/>
      <polygon points="98,28 130,16 130,40" fill="var(--teal-light)"/>
      <polygon points="0,405 70,385 130,385 130,392 40,424 0,424" fill="var(--yellow)"/>
      <polygon points="0,424 0,400 90,370 130,372 60,424" fill="var(--teal-dark)"/>
      <polygon points="60,424 130,392 130,424" fill="var(--teal)"/>
    </svg>
    <div class="portrait" role="img" aria-label="Porträtfoto von Dr. Lukas Brandt"></div>
    <h1 class="role-title">Chief Digital Officer<br>Digital Leader</h1>
    <dl class="facts">
      <dt>Dr. Lukas Brandt</dt><dd>Chief Information Officer (CIO) | Ph.D.<br>Wirtschaftsinformatik</dd>
      <dt>Adresse</dt><dd>Lindenweg 14<br>10115 Berlin</dd>
      <dt>Geburtsdaten</dt><dd>29. März 1978 in Konstanz</dd>
      <dt>Familienstand</dt><dd>verheiratet | 2 Kinder</dd>
      <dt>Mobil</dt><dd>+49 (0) 170 55 0192 40</dd>
      <dt>E-Mail</dt><dd>kontakt@brandt-mail.de</dd>
      <dt>Profil</dt><dd>https://www.brandt-profil.de/</dd>
    </dl>
  </aside>
  <div class="overview">
    <h2 class="section-title">Auf einen Blick</h2>
    <ul>
      <li><b>Kommunikationsstarke Führungspersönlichkeit</b> mit mehrjähriger Erfahrung in Leitungsfunktionen im <b>IT-Bereich</b>, aktuell <b>Chief Information Officer (CIO)</b> und <b>Chief Digital Officer (CDO)</b></li>
      <li>Umfangreiche <b>Fachexpertise</b> in: Konzeption und <b>Weiterentwicklung von IT-Unternehmensstrategien</b> | Effizienzsteigerung im IT-Bereich | <b>Optimierung der IT-Service-Strukturen</b> | Planung und Durchführung <b>konzernweiter IT-Programme</b></li>
      <li>Experte auf dem Gebiet der <b>Transformation von Unternehmen in die digitale Welt</b> (Industrie 4.0) | <b>Etablierung der IT als Business Enabler</b></li>
      <li>Führung von <b>75 MA + ca. 20 (weltweite und externe)</b>, davon 4 Führungskräfte | Budget i.H.v. <b>22 Mio. €</b> p.a.</li>
      <li><b>Wissensmanager</b> mit <b>interkultureller Kompetenz</b>, breitem Technologieverständnis sowie ausgeprägter Durchsetzungs- und Teamfähigkeit</li>
      <li><b>umsetzungsstark</b> | lösungsorientiert | <b>unternehmerisch</b> | visionär</li>
    </ul>
  </div>
</section>

<!-- Page 2 -->
<section class="page page--2">
  <svg class="deco" width="375" height="485" viewBox="0 0 375 485" aria-hidden="true">
    <polygon points="0,0 375,0 375,24 0,52" fill="var(--teal)"/>
    <polygon points="120,40 375,12 375,22 160,38" fill="var(--yellow)"/>
    <polygon points="250,26 375,0 375,12" fill="var(--teal-light)"/>
    <polygon points="170,485 375,432 375,485" fill="var(--teal)"/>
    <polygon points="265,470 320,446 375,442 330,466" fill="var(--yellow)"/>
  </svg>
  <div class="running-head"><strong>Dr. Lukas Brandt</strong>+49 (0) 170 55 0192 40<br>kontakt@brandt-mail.de</div>
  <div class="content" style="top:68px">
    <div class="heading-box">Berufliche Erfahrungen</div>
    <div class="entry">
      <div class="when">10/2012 - heute</div>
      <div class="what">
        <b>Halvorsen Gruppe</b> | Albstadt | www.halvorsen-gruppe.de<br>Weltweiter Hersteller von zerspanenden Präzisionswerkzeugen | 7.000 MA weltweit in ca. 50 Ländern | 900 Mio. € Umsatz
        <div class="label">Chief Information Officer/ Chief Digital Officer</div>
        <ul>
          <li>Verantwortung der operativen sowie strategischen IT weltweit</li>
          <li>Verantwortung der digitalen Transformation der Firma weltweit, Umsetzung der Vision 2020</li>
          <li>Aufbau einer IT-Strategie in Abstimmung mit Geschäftsführung und Eigentümer</li>
          <li>Entwicklung und Umsetzung einer ERP-Roadmap 2020, inkl. Einführung einer neuen ERP-Suite in ca. 40 Tochtergesellschaften weltweit</li>
          <li>Aufbau eines IT-Risikomanagementsystems in Zusammenhang mit IT-GRC-Strukturen</li>
          <li>Definition einer zentralen e-Business Multichannel Architektur</li>
          <li>Aufbau einer IT-Leistungsrechnung sowie eines IT-Controllings</li>
          <li>Aufbau zweier IT Hubs in Asien und Amerika</li>
          <li>Neuausrichtung der gesamten IT-Infrastruktur (Migration der Verzeichnisdienste)</li>
          <li>Etablierung einer IT-Projektmethodik</li>
          <li>Erarbeitung eines ECM-Konzepts „Just-in-time Informationslogistik“</li>
          <li>Definition/Rollout einer Prozessmodellierungssystematik nach gängiger Prozessnotation</li>
          <li>Aufteilung der IT in Projektgeschäft und Katalog bzw. Standardgeschäft (vom Einkauf über Anforderungen bis hin zum Betrieb)</li>
          <li>Definition einer neuen IT-Organisation nach dem Plan-Build-Run Prinzip eines Betriebsrahmenwerks</li>
          <li>Entwicklung einer Roadmap Industrie 4.0, Erprobung diverser Industrie-4.0-Themen mit der Produktion, Erarbeitung einer IT-Security-Strategie für alle Produktionswerke, Testen von neuen „Wearables“ zum Einsatz in der Produktion</li>
          <li>Aufbau einer neuen digitalen Einheit zur Erarbeitung von neuen Geschäftsmodellen</li>
        </ul>
        <div class="label">Verantwortung:</div>
        Führung von 75 MA + ca. 20 (weltweite und externe), davon 4 Führungskräfte | Budget i.H.v. 22 Mio. €
        <div class="label">Erfolge:</div>
        <ul>
          <li>Einführung einer globalen ERP-Strategie, Einsparung von 1/3 der Kosten bei jedem Rollout durch Einsatz einer Mittelstandslösung, Verkürzung der Einführungszeiten von 1 Jahr auf 4 Monate sowie Erhöhung der Userzufriedenheit durch größere Usability</li>
          <li>Erstellung und Umsetzung einer globalen IT-Strategie und komplette Neustrukturierung der IT zu einer schnelleren und agileren Ebene (Etablierung einer Two Speed IT)</li>
          <li>Erstellung einer digitalen Vision 2020</li>
          <li>Erzielung erster Online-Umsätze mit dem neuen eBusiness Konzept</li>
        </ul>
      </div>
    </div>
  </div>
  <div class="page-no">2</div>
</section>

<!-- Page 3 -->
<section class="page page--3">
  <svg class="deco" width="375" height="485" viewBox="0 0 375 485" aria-hidden="true">
    <polygon points="0,0 375,0 375,24 0,52" fill="var(--teal)"/>
    <polygon points="120,40 375,12 375,22 160,38" fill="var(--yellow)"/>
    <polygon points="250,26 375,0 375,12" fill="var(--teal-light)"/>
    <polygon points="170,485 375,432 375,485" fill="var(--teal)"/>
    <polygon points="265,470 320,446 375,442 330,466" fill="var(--yellow)"/>
  </svg>
  <div class="running-head"><strong>Dr. Lukas Brandt</strong>+49 (0) 170 55 0192 40<br>kontakt@brandt-mail.de</div>
  <div class="content" style="top:96px">
    <div class="entry">
      <div class="when"></div>
      <div class="what">
        <div class="label" style="margin-top:0">Verantwortung:</div>
        Führung von 4 MA | Budget i.H.v. 2 Mio. €
        <div class="label">Erfolge:</div>
        <ul>
          <li>Prozessoptimierungen und Einsparungen in allen Unternehmensbereichen sowie Upgrade des bestehenden ERP Systems</li>
          <li>Erhöhung der Anwenderzufriedenheit von Schulnote 4 auf 1,5</li>
          <li>Senkung der IT-Kosten um 20%</li>
        </ul>
      </div>
    </div>
    <div class="entry"><div class="when">07/2006 - 03/2008</div><div class="what"><b>Nordfeld Software GmbH</b> | Donaueschingen | Projektleiter, Business Consultant Nordfeld ERP</div></div>
    <div class="entry"><div class="when">03/2005 - 06/2006</div><div class="what"><b>Corvia GmbH</b> | Alsdorf | Key Account Manager</div></div>
    <div class="entry"><div class="when">03/2004 - 02/2005</div><div class="what"><b>Veltaris Enterprise Solutions GmbH</b> | Villingen-Schwenningen | Junior Account Manager</div></div>
    <div class="heading-box heading-box--wide">Ausbildung</div>
    <div class="entry"><div class="when">09/2010 - 08/2014</div><div class="what"><b>Ph.D. in Business Management</b> | Danubia Universität<br>Dissertation: „Effective deployment of ERP in small and medium-size companies to get a decisive competitive edge“</div></div>
    <div class="entry"><div class="when">04/2006 - 10/2008</div><div class="what"><b>Master of Business Consulting (MBC)</b> | Fernhochschule Nordhafen, Standort Frankfurt<br>Schwerpunkte: strategische Unternehmensberatung, KMU Controlling, Personalberatung und Coaching, Prozess- und Organisationsberatung, Corporate Finance-Beratung<br>Thesis: „US-Bilanzrecht and the conversion in the IT sector of a middle-class enterprise with corporate affiliation“ | Note: 2,2</div></div>
    <div class="entry"><div class="when">10/2000 - 06/2003</div><div class="what"><b>Diplom-Wirtschaftsinformatiker (DH)</b> | Duale Hochschule Südland, Berufsakademie Talheim und Nordfeld AG in Hüfingen<br>Schwerpunkte: E-Business und Consulting<br>Diplomarbeit: „Bedarfsanalyse betriebswirtschaftlicher Funktionalitäten als Basis für den Produktplanungsprozess bei Bestandskunden.“ | Note: 1,5</div></div>
  </div>
  <div class="page-no">3</div>
</section>

<!-- Page 4 -->
<section class="page page--4">
  <svg class="deco" width="375" height="485" viewBox="0 0 375 485" aria-hidden="true">
    <polygon points="0,0 375,0 375,24 0,52" fill="var(--teal)"/>
    <polygon points="120,40 375,12 375,22 160,38" fill="var(--yellow)"/>
    <polygon points="250,26 375,0 375,12" fill="var(--teal-light)"/>
    <polygon points="170,485 375,432 375,485" fill="var(--teal)"/>
    <polygon points="265,470 320,446 375,442 330,466" fill="var(--yellow)"/>
  </svg>
  <div class="running-head"><strong>Dr. Lukas Brandt</strong>+49 (0) 170 55 0192 40<br>kontakt@brandt-mail.de</div>
  <div class="content" style="top:96px">
    <div class="entry"><div class="when">07/2000 - 07/1999</div><div class="what">Zivildienst | Berufsförderungszentrum | Möhringen</div></div>
    <div class="entry"><div class="when">07/1999</div><div class="what">Allgemeine Hochschulreife | Technisches Gymnasium | Tuttlingen</div></div>
    <div class="heading-box">Fort- und Weiterbildungen</div>
    <div class="entry"><div class="when">Führung/<br>Management</div><div class="what">Teilnahme an Veranstaltungen und Workshops zu <b>Führung und Management</b>, wie z.B.:
      <ul>
        <li>Management- und Personalführungsseminar | Varnholt Gruppe | 2011</li>
        <li>Management- und Personalführungsseminar | Klimatec Nord | 2008</li>
        <li>Feedbackgespräche, Coaching von Mitarbeitern</li>
        <li>Persönlichkeitsmodell zur Einschätzung von Mitarbeitern</li>
      </ul></div></div>
    <div class="heading-box">Auszeichnungen</div>
    <div class="entry"><div class="when">CIO des<br>Jahres 2015</div><div class="what">
      <div class="kv"><b>Anwendungsbezogen</b><span>: Office-Paket | Projektplanung | Prozessmodellierung | Projektportal</span></div>
      <div class="kv"><b>Fachbezogen</b><span>: ERP-Suite | Nordfeld ERP | CRM-Suite | Web-Plattformen</span></div>
      <div class="kv"><b>Programmiersprachen</b><span>: Objektorientiert | Skriptsprachen | Datenbanken | ERP-Entwicklung</span></div>
    </div></div>
    <div class="entry"><div class="when">Sprachkenntnisse</div><div class="what"><div class="kv"><b>Deutsch</b><span>: Muttersprache | Englisch: verhandlungssicher</span></div></div></div>
    <div class="heading-box">Weitere Angaben</div>
    <div class="entry"><div class="when">Ausland</div><div class="what">Auslandspraktikum bei Nordfeld infotech Ltd. in Ahmedabad (Indien)</div></div>
    <div class="entry"><div class="when">Interessen</div><div class="what"><div class="kv"><b>Sport</b><span>: Fußball sowie jeglicher Ballsport, Fitness | Kochen | Reisen</span></div></div></div>
    <div class="entry"><div class="when"></div><div class="what"><span class="sign-off">— Berlin, 9. März 2017 —</span></div></div>
  </div>
  <div class="page-no">4</div>
</section>

</body>
</html>
```